Updated Package Design for FloraPeak

1. We have a package that we are manufacturing. It has been well recieved and everybody likes it.

2. We have a client in the EU who wants some design changes. Something more suited to their clientele. Young and hip, I am told. Basically this product will be sold as an accessory to Sports Water Bottles. So it will be hanging on clip strips next to the bottles.

3. Attached we have the current design w/ dimensions attached and the EU package idea as well.

4. What we want is a FRESH LOOK at the text and a HYBRID of the two. Look at the brief.

5. What we don't want to do is TOTALLY change everything (because I'll have to change EVERYTHING downstream attached to it and I don't want to do that)

6. Attached files are a version of the brief w/ images. front and back AI files of the current package.

View product online:

http://theflorapeak-example.com/

Target Market(s)

Industry/Entity Type

Water Treatment

Font styles to use
Sans Serif

Requirements
Must have
• Clean, fresh, green, healthy and hip.
Nice to have
• 4. What we want is a FRESH LOOK at the text and a HYBRID of the two. Look at the brief.
Should not have
• 5. What we don't want to do is TOTALLY change everything (because I'll have to change EVERYTHING downstream attached to it and I don't want to do that)

```html
<!DOCTYPE html>
<html lang="en">
<head>
<meta charset="utf-8">
<title>FloraPeak package front</title>
<link rel="stylesheet" href="https://fonts.googleapis.com/css2?family=Open+Sans:wght@400;600;700&family=Source+Code+Pro:wght@700&display=swap">
<style>
  :root {
    --backdrop: #8c8c8c;
    --pack-white: #ffffff;
    --pack-edge: #d9d9d9;
    --cap-orange: #f07a2e;
    --cap-orange-dark: #d85f17;
    --brand-grey: #6a6a6a;
    --brand-dot: #2f8fc6;
    --splash-light: #e9f4fb;
    --splash-mid: #7fb9dc;
    --splash-deep: #2c6fa3;
    --badge-red: #e8402a;
    --badge-red-dark: #c42a17;
    --type-blue: #1f55b8;
    --wave-blue: #1d66c9;
    --recycle-blue: #3f6fa0;
    --caption: #ffffff;
  }
  html, body {
    margin: 0;
    padding: 0;
    overflow: hidden;
  }
  body {
    width: 851px;
    height: 1200px;
    background: var(--backdrop);
    font-family: "Open Sans", Arial, sans-serif;
    position: relative;
  }
  .package {
    position: absolute;
    left: 0;
    top: 0;
    width: 851px;
    height: 1200px;
  }
  .brand {
    position: absolute;
    top: 258px;
    left: 0;
    width: 851px;
    display: flex;
    justify-content: center;
    align-items: center;
    gap: 10px;
  }
  .brand-dot {
    width: 34px;
    height: 34px;
    border-radius: 50%;
    background: var(--brand-dot);
  }
  .brand-name {
    font-weight: 600;
    font-size: 40px;
    color: var(--brand-grey);
    letter-spacing: -0.5px;
  }
  .splash {
    position: absolute;
    left: 213px;
    top: 330px;
    width: 427px;
    height: 70px;
    background: linear-gradient(90deg, var(--splash-light) 0%, var(--splash-mid) 40%, var(--splash-deep) 65%, var(--splash-light) 100%);
    border-radius: 40px;
    opacity: 0.85;
  }
  .badge {
    position: absolute;
    left: 304px;
    top: 377px;
    width: 249px;
    height: 133px;
    border-radius: 22px;
    background: linear-gradient(180deg, var(--badge-red) 0%, var(--badge-red-dark) 100%);
    color: #fff;
    text-align: center;
    display: flex;
    flex-direction: column;
    justify-content: center;
    line-height: 1;
  }
  .badge-strong {
    font-weight: 700;
    font-size: 42px;
    letter-spacing: 1px;
  }
  .badge-soft {
    font-weight: 400;
    font-size: 30px;
    letter-spacing: 3px;
    margin: 3px 0;
  }
  .tagline {
    position: absolute;
    left: 0;
    top: 990px;
    width: 851px;
    text-align: center;
    font-family: "Source Code Pro", "Courier New", monospace;
    font-weight: 700;
    font-size: 27px;
    line-height: 1.2;
    color: var(--type-blue);
  }
  .caption {
    position: absolute;
    left: 0;
    top: 1162px;
    width: 851px;
    text-align: center;
    font-size: 16px;
    color: var(--caption);
  }
</style>
</head>
<body>
  <svg class="package" viewBox="0 0 851 1200" aria-hidden="true">
    <path class="die-cut" fill="var(--pack-white)" stroke="var(--pack-edge)" stroke-width="1.5"
      d="M300 28 H551 Q567 28 567 44 V160
         C567 230 681 230 681 300 V560
         C681 600 659 610 659 650 V730
         C659 770 681 780 681 820 V1110
         Q681 1140 651 1140 H200 Q170 1140 170 1110 V820
         C170 780 192 770 192 730 V650
         C192 610 170 600 170 560 V300
         C170 230 283 230 283 160 V44 Q283 28 300 28 Z"/>
    <rect class="hang-hole" x="395" y="40" width="60" height="16" rx="8" fill="var(--backdrop)"/>
    <rect class="cap" x="300" y="70" width="252" height="56" rx="6" fill="var(--cap-orange)"/>
    <rect class="cap-seal" x="300" y="70" width="252" height="10" rx="4" fill="var(--cap-orange-dark)"/>
    <text x="355" y="100" font-family="Open Sans, sans-serif" font-size="8" fill="#fff">TEAR HERE</text>
    <text x="445" y="100" font-family="Open Sans, sans-serif" font-size="8" fill="#fff">RESEAL HERE</text>
    <path class="wave wave-top" d="M255 982 Q425 968 596 982" fill="none" stroke="var(--wave-blue)" stroke-width="5" stroke-linecap="round"/>
    <path class="wave wave-bottom" d="M255 1058 Q425 1072 596 1054" fill="none" stroke="var(--wave-blue)" stroke-width="5" stroke-linecap="round"/>
    <g class="recycle-icon" fill="none" stroke="var(--recycle-blue)" stroke-width="4" stroke-linecap="round" stroke-linejoin="round">
      <path d="M418 1080 L425 1070 L432 1080"/>
      <path d="M425 1070 L437 1090"/>
      <path d="M440 1098 L426 1098"/>
      <path d="M430 1093 L425 1098 L430 1103"/>
      <path d="M412 1098 L419 1086"/>
      <path d="M414 1083 L420 1086 L423 1080"/>
    </g>
  </svg>

  <div class="brand">
    <span class="brand-dot"></span>
    <span class="brand-name">FloraPeak</span>
  </div>

  <div class="splash" role="img" aria-label="Splash of clear blue water"></div>

  <div class="badge">
    <span class="badge-strong">INSERT</span>
    <span class="badge-soft">SWIRL</span>
    <span class="badge-strong">DRINK</span>
  </div>

  <p class="tagline" style="margin:0">Portable water pufier<br>for your tap water</p>

  <p class="caption" style="margin:0">FloraPeak package front</p>
</body>
</html>
```